Beacon Advisory Website

I currently have a website www.beaconadvisoryinc.example. We are a IT Consulting Company. Our website will pretty much tell out our services. I am looking to enhance my website and make it look more professional. Looking for very classy and Contemporary look and design for my website.

Industry/Entity Type

It Company

```html
<!DOCTYPE html>
<html lang="en">
<head>
<meta charset="utf-8">
<title>Beacon Advisory</title>
<link href="https://fonts.googleapis.com/css2?family=Open+Sans:wght@400;600;700&display=swap" rel="stylesheet">
<style>
:root{
  --navy:#1c3d6e;
  --blue:#1565a8;
  --accent:#1a7cc2;
  --text:#444a52;
  --muted:#5b6168;
  --footer:#1f3b60;
  --footer-deep:#17304f;
  --icon-dark:#1a2b45;
  --white:#ffffff;
}
*{margin:0;padding:0;box-sizing:border-box}
html,body{width:1200px;height:2308px;overflow:hidden;background:var(--white)}
body{position:relative;font-family:"Open Sans",Arial,sans-serif;color:var(--text)}
.abs{position:absolute}

/* header */
.site-header{position:absolute;left:0;top:0;width:1200px;height:105px;background:var(--white)}
.brand{position:absolute;left:62px;top:30px;display:flex;align-items:center;gap:12px}
.brand-mark{width:40px;height:40px;background:var(--accent);border-radius:4px}
.brand-name{font-weight:700;font-size:24px;color:var(--accent);letter-spacing:.3px}
.main-nav{position:absolute;top:52px;left:496px;display:flex;gap:0}
.main-nav a{font-size:17px;color:#4a4f55;text-decoration:none;position:absolute;white-space:nowrap}

/* hero */
.hero{position:absolute;left:2px;top:105px;width:1196px;height:347px;
  background:linear-gradient(100deg,#2f8aa0 0%,#7fc3cc 35%,#c9b8a4 55%,#6fb3c2 75%,#3b5f7a 100%)}

/* services */
.section-kicker{position:absolute;left:482px;top:500px;font-size:23px;color:#4a4f55}
.section-title{position:absolute;left:482px;top:520px;font-size:39px;color:var(--navy);font-weight:400}
.rule{position:absolute;height:4px;background:var(--accent)}
.service{position:absolute;top:620px;width:310px}
.service-head{display:flex;align-items:center;gap:14px;height:50px}
.service-title{font-size:21px;font-weight:600;color:#333}
.service-title.is-active{color:var(--accent)}
.service-body{margin-top:18px;font-size:15.5px;line-height:21.5px;color:#333}
.read-more{position:absolute;font-size:15.5px;color:#333;display:flex;align-items:center;gap:8px}
.read-more.is-active{color:var(--accent)}

/* who we are */
.about-band{position:absolute;left:2px;top:857px;width:1196px;height:358px;background:var(--blue)}
.about-photo{position:absolute;left:2px;top:857px;width:1196px;height:358px}
.about-title{position:absolute;left:599px;top:893px;font-size:29px;color:var(--white);font-weight:400}
.about-body{position:absolute;left:601px;top:936px;width:545px;font-size:16.4px;line-height:21.8px;color:#e6eef7}
.about-link{position:absolute;left:601px;top:1113px;font-size:16px;color:var(--white)}

/* features */
.features-title{position:absolute;left:0;width:1190px;top:1257px;text-align:center;font-size:36px;color:var(--navy);font-weight:400}
.feature{position:absolute;width:300px;text-align:center}
.feature-icon{width:82px;height:82px;border-radius:50%;background:var(--icon-dark);margin:0 auto}
.feature-name{margin-top:13px;font-size:24px;color:#555a60}
.feature-text{margin-top:14px;font-size:15.5px;line-height:21.4px;color:var(--muted)}

/* footer */
.footer-bg{position:absolute;left:0;top:0}
.footer-head{position:absolute;top:1979px;font-size:16px;font-weight:700;color:var(--white);letter-spacing:.3px}
.footer-links{position:absolute;top:2022px;list-style:none}
.footer-links li{font-size:12px;font-weight:600;color:#c9d6e6;height:35px;letter-spacing:.3px}
.contact-line{position:absolute;left:606px;font-size:12px;font-weight:600;color:#c9d6e6;line-height:16.5px}
.footer-brand{position:absolute;left:846px;top:2022px;display:flex;align-items:center;gap:14px}
.footer-brand .brand-mark{width:56px;height:56px;background:var(--white)}
.footer-brand .brand-name{color:var(--white);font-size:30px}
.social{position:absolute;width:32px;height:32px;border:2px solid #dbe4ef;border-radius:50%;top:2202px}
.copyright{position:absolute;right:62px;top:2251px;font-size:13px;font-weight:600;color:#dbe4ef}
</style>
</head>
<body>

<header class="site-header">
  <div class="brand"><span class="brand-mark"></span><span class="brand-name">Beacon Advisory</span></div>
  <nav class="main-nav">
    <a style="left:0">Company</a>
    <a style="left:118px">Services</a>
    <a style="left:222px">Solutions</a>
    <a style="left:339px">Resources</a>
    <a style="left:464px">Career</a>
    <a style="left:555px">Contact Us</a>
  </nav>
</header>

<div class="hero" role="img" aria-label="Photo of two business people shaking hands"></div>

<section class="services">
  <div class="rule" style="left:384px;top:529px;width:68px"></div>
  <div class="section-kicker">Our Services</div>
  <h2 class="section-title">We support this Services</h2>

  <div class="service" style="left:90px">
    <div class="service-head">
      <svg width="72" height="36" viewBox="0 0 72 36"><rect x="4" y="10" width="30" height="16" rx="6" fill="#555"/><rect x="38" y="10" width="30" height="16" rx="6" fill="#555"/><rect x="24" y="12" width="24" height="12" rx="6" fill="#777"/></svg>
      <span class="service-title">Consulting</span>
    </div>
    <p class="service-body">Beacon Advisory has certified profes-sional consultants to work with you to help increase the business by providing IT services ...</p>
  </div>
  <div class="read-more" style="left:89px;top:784px">Read More <svg width="18" height="10" viewBox="0 0 18 10"><path d="M0 5h15M11 1l4 4-4 4" stroke="currentColor" stroke-width="1.8" fill="none"/></svg></div>

  <div class="service" style="left:462px">
    <div class="service-head">
      <svg width="42" height="50" viewBox="0 0 42 50"><circle cx="21" cy="30" r="16" fill="none" stroke="var(--accent)" stroke-width="6"/><circle cx="21" cy="30" r="5" fill="var(--accent)"/><path d="M21 2c5 6 8 9 8 14H13c0-5 3-8 8-14z" fill="var(--accent)"/></svg>
      <span class="service-title is-active">Staff Augmentation</span>
    </div>
    <p class="service-body">For years Beacon Advisory as been offering our customers the ability to augment their existing staff ...</p>
  </div>
  <div class="read-more is-active" style="left:462px;top:781px">Read More <svg width="18" height="10" viewBox="0 0 18 10"><path d="M0 5h15M11 1l4 4-4 4" stroke="currentColor" stroke-width="1.8" fill="none"/></svg></div>

  <div class="service" style="left:817px">
    <div class="service-head">
      <svg width="44" height="44" viewBox="0 0 44 44"><g fill="#555"><circle cx="22" cy="22" r="15"/><rect x="19" y="1" width="6" height="10"/><rect x="19" y="33" width="6" height="10"/><rect x="1" y="19" width="10" height="6"/><rect x="33" y="19" width="10" height="6"/><rect x="19" y="1" width="6" height="10" transform="rotate(45 22 22)"/><rect x="19" y="33" width="6" height="10" transform="rotate(45 22 22)"/><rect x="1" y="19" width="10" height="6" transform="rotate(45 22 22)"/><rect x="33" y="19" width="10" height="6" transform="rotate(45 22 22)"/></g><circle cx="22" cy="22" r="8" fill="#fff"/><circle cx="22" cy="22" r="4" fill="#555"/></svg>
      <span class="service-title">Offshore</span>
    </div>
    <p class="service-body">Our Offshore development model has a unique distinction of providing effi-cient software solutions</p>
  </div>
  <div class="read-more" style="left:902px;top:787px"><svg width="18" height="10" viewBox="0 0 18 10"><path d="M0 5h15M11 1l4 4-4 4" stroke="currentColor" stroke-width="1.8" fill="none"/></svg></div>
</section>

<section class="about">
  <div class="about-band"></div>
  <svg class="about-photo" width="1196" height="358" viewBox="0 0 1196 358" role="img" aria-label="Photo of a hand touching a digital city interface">
    <defs><linearGradient id="aboutTone" x1="0" y1="0" x2="1" y2="1"><stop offset="0" stop-color="#eef4f9"/><stop offset=".5" stop-color="#a9cde6"/><stop offset="1" stop-color="#4d93c8"/></linearGradient></defs>
    <polygon points="0,0 521,0 390,358 0,358" fill="#dfe9f2"/>
    <polygon points="0,0 514,0 383,350 0,350" fill="url(#aboutTone)"/>
  </svg>
  <div class="rule" style="left:513px;top:914px;width:68px;height:3px;background:#b7c7d8"></div>
  <h2 class="about-title">WHO WE ARE</h2>
  <p class="about-body">Today’s IT market is a dynamic, fast-paced industry, with ever-increasing demands. Meeting these demands for over 25 years, Beacon Advisory maintains a global presence, aggressively recruiting expertly qualified IT and Management Professionals from around the world and cultivating key partnerships with corporations to understand their business models end-to-end, with a goal of delivering exceptional client service and ensur-ing a consistent delivery of the talent needed to drive results.</p>
  <div class="about-link">Read More</div>
</section>

<section class="features">
  <div class="rule" style="left:307px;top:1283px;width:69px"></div>
  <div class="rule" style="left:830px;top:1283px;width:68px"></div>
  <h2 class="features-title">SOME KINGAL FEATURES</h2>

  <div class="feature" style="left:110px;top:1354px"><div class="feature-icon"></div><div class="feature-name">Technology</div><p class="feature-text">Lorem ipsum dolor sit amet, consecte-tur adipisicing elit. Excepturi perferen-dis magnam ea necessitatibus, officiis voluptas odit.</p></div>
  <div class="feature" style="left:436px;top:1354px"><div class="feature-icon"></div><div class="feature-name">Business</div><p class="feature-text">Lorem ipsum dolor sit amet, consecte-tur adipisicing elit. Excepturi perferen-dis magnam ea necessitatibus, officiis voluptas odit.</p></div>
  <div class="feature" style="left:764px;top:1354px"><div class="feature-icon"></div><div class="feature-name">Application</div><p class="feature-text">Lorem ipsum dolor sit amet, consecte-tur adipisicing elit. Excepturi perferen-dis magnam ea necessitatibus, officiis voluptas odit.</p></div>

  <div class="feature" style="left:110px;top:1634px"><div class="feature-icon"></div><div class="feature-name">Developement</div><p class="feature-text">Lorem ipsum dolor sit amet, consecte-tur adipisicing elit. Excepturi perferen-dis magnam ea necessitatibus, officiis voluptas odit.</p></div>
  <div class="feature" style="left:436px;top:1634px"><div class="feature-icon"></div><div class="feature-name">Enterprise Integration</div><p class="feature-text">Lorem ipsum dolor sit amet, consecte-tur adipisicing elit. Excepturi perferen-dis magnam ea necessitatibus, officiis voluptas odit.</p></div>
  <div class="feature" style="left:764px;top:1634px"><div class="feature-icon"></div><div class="feature-name">IT Consulting</div><p class="feature-text">Lorem ipsum dolor sit amet, consecte-tur adipisicing elit. Excepturi perferen-dis magnam ea necessitatibus, officiis voluptas odit.</p></div>
</section>

<footer class="site-footer">
  <svg class="footer-bg" width="1200" height="2308" viewBox="0 0 1200 2308">
    <polygon points="2,1907 1198,1925 1198,2308 2,2308" fill="var(--footer)"/>
    <polygon points="653,2308 1198,2035 1198,2308" fill="var(--footer-deep)"/>
    <line x1="653" y1="2308" x2="1198" y2="2035" stroke="#6f8fb5" stroke-width="2"/>
  </svg>

  <div class="footer-head" style="left:64px">INFORMATION</div>
  <ul class="footer-links" style="left:64px">
    <li>COMPANY</li><li>SERVICES</li><li>SOLUTIONS</li><li>RESOURCES</li><li>CAREER</li><li>CONTACT US</li>
  </ul>

  <div class="footer-head" style="left:304px">CUSTOMER SERVICE</div>
  <ul class="footer-links" style="left:308px">
    <li>HELP &amp; CONTACT</li><li>RETURN POLICY</li><li>CAREERS</li><li>AFFILITES</li><li>LEGAL NOTICE</li><li>PRIVACY POLICY</li>
  </ul>

  <div class="footer-head" style="left:573px">CONTACT US</div>
  <svg class="abs" style="left:571px;top:2023px" width="12" height="17" viewBox="0 0 12 17"><path d="M6 0a6 6 0 0 0-6 6c0 4.5 6 11 6 11s6-6.5 6-11a6 6 0 0 0-6-6z" fill="#fff"/><circle cx="6" cy="6" r="2.2" fill="var(--footer)"/></svg>
  <div class="contact-line" style="top:2022px">120 HARBOR LANE<br>SUITE 310<br>MILLBROOK, NJ 07999</div>
  <svg class="abs" style="left:571px;top:2096px" width="16" height="16" viewBox="0 0 16 16"><path d="M3.5 0.5l2.5 3.2-1.6 2a10 10 0 0 0 5.9 5.9l2-1.6 3.2 2.5-1.5 3C7 15 1 9 0.5 2z" fill="#fff"/></svg>
  <div class="contact-line" style="top:2096px">1 (555) 014 2290</div>
  <svg class="abs" style="left:571px;top:2138px" width="19" height="14" viewBox="0 0 19 14"><rect x="1" y="1" width="17" height="12" rx="1.5" fill="none" stroke="#fff" stroke-width="1.8"/><path d="M1.5 2l8 6 8-6" fill="none" stroke="#fff" stroke-width="1.8"/></svg>
  <div class="contact-line" style="top:2137px">info@BeaconAdvisory.example</div>

  <div class="footer-brand"><span class="brand-mark"></span><span class="brand-name">Beacon Advisory</span></div>

  <span class="social" style="left:894px"></span>
  <span class="social" style="left:936px"></span>
  <span class="social" style="left:979px"></span>
  <span class="social" style="left:1021px"></span>
  <span class="social" style="left:1065px"></span>

  <div class="copyright">Copyright @ Beacon Advisory</div>
</footer>

</body>
</html>
```